BRAVEN POWERLINE SERVICES needs a vibrant design for electrical contracting work.

I require a card design for my own electrical contracting business. I will be doing a lot of domestic and commercial work, including things such as repairs, maintenance, lighting, installations and various others. LED lighting and energy efficiency will be a big part of my business. I wish not to have childish pictures such as light bulbs in the design, but rather a smart and modern looking card which incorporates my logo colours and perhaps the same lighting strike within the faded background of the card.

Target Market(s)

Residential and Commercial property owners.

Industry/Entity Type

Electrical

Contact Information for Business Card

Dalen Voskic
EC40923
Phone Number: 0417 358 942
Email: dalen@bravenpowerline.com

Font styles to use
Serif
Sans Serif

Requirements
Must have
• My Logo and associated colours.
Nice to have
• Some form of shapes splitting the card into different colours related to the colours of my logo. Electric Blue, Silver/Grey and White.
Should not have
• Childish pictures and symbols such as light bulbs.

```html
<!DOCTYPE html>
<html lang="en">
<head>
<meta charset="utf-8">
<title>Braven Powerline Services – Business Card</title>
<link rel="stylesheet" href="https://fonts.googleapis.com/css2?family=Michroma&family=Lato:wght@400&display=swap">
<style>
  :root {
    --backdrop: #1b1b1d;
    --electric-blue: #2c2fa3;
    --lavender: #8a88e6;
    --graphite: #5c5c60;
    --graphite-dark: #3e3e42;
    --ink: #050505;
    --white: #ffffff;
    --silver-light: #f4f4f6;
    --silver: #cfd0d4;
  }
  * { box-sizing: border-box; margin: 0; padding: 0; }
  html, body {
    width: 1200px; height: 871px; overflow: hidden;
    background: var(--backdrop);
  }
  .sheet {
    width: 1200px; height: 871px;
    display: flex; flex-direction: column; align-items: center; justify-content: center;
    gap: 40px;
  }
  .card {
    position: relative;
    width: 620px; height: 379px;
    overflow: hidden;
    box-shadow: 0 12px 30px rgba(0,0,0,.6);
  }
  .card svg.card-art { position: absolute; inset: 0; width: 100%; height: 100%; }

  /* Wordmark */
  .wordmark {
    position: absolute;
    display: flex; align-items: center;
    color: var(--electric-blue);
    font-family: "Michroma", sans-serif;
    font-weight: 400;
  }
  .wordmark .mark-dot {
    border: 5px solid var(--electric-blue);
    border-radius: 50%;
    flex: none;
  }
  .wordmark .name { display: flex; flex-direction: column; line-height: 1; }
  .wordmark .name-main { letter-spacing: .02em; }
  .wordmark .name-sub { letter-spacing: .03em; }

  /* Back */
  .card-back { background: linear-gradient(160deg, var(--silver-light) 0%, var(--white) 45%, var(--silver) 100%); }
  .card-back .wordmark { left: 70px; top: 132px; gap: 20px; }
  .card-back .mark-dot { width: 96px; height: 96px; border-width: 7px; }
  .card-back .name-main { font-size: 62px; }
  .card-back .name-sub { font-size: 19px; margin-top: 8px; }

  /* Front */
  .card-front .wordmark { left: 360px; top: 162px; gap: 10px; }
  .card-front .mark-dot { width: 48px; height: 48px; }
  .card-front .name-main { font-size: 31px; }
  .card-front .name-sub { font-size: 9.5px; margin-top: 5px; }

  .contact {
    position: absolute; left: 44px; top: 150px;
    color: var(--white);
  }
  .contact .person {
    font-family: "Michroma", sans-serif;
    font-size: 15px; letter-spacing: .22em;
  }
  .contact .licence {
    font-family: "Michroma", sans-serif;
    font-size: 12px; letter-spacing: .3em;
    color: var(--lavender);
    margin-top: 6px;
  }
  .contact .line {
    display: flex; align-items: center; gap: 8px;
    font-family: "Lato", sans-serif; font-size: 13.5px;
    margin-top: 6px;
  }
  .contact .line svg { width: 10px; height: 10px; flex: none; }
</style>
</head>
<body>
<main class="sheet">

  <section class="card card-back" aria-label="Card back">
    <div class="wordmark">
      <span class="mark-dot"></span>
      <span class="name">
        <span class="name-main">BRAVEN</span>
        <span class="name-sub">POWERLINE SERVICES</span>
      </span>
    </div>
  </section>

  <section class="card card-front" aria-label="Card front">
    <svg class="card-art" viewBox="0 0 620 379" preserveAspectRatio="none" aria-hidden="true">
      <defs>
        <linearGradient id="graphite-fade" x1="0" y1="0" x2="1" y2="1">
          <stop offset="0" stop-color="var(--graphite)"/>
          <stop offset="1" stop-color="var(--graphite-dark)"/>
        </linearGradient>
      </defs>
      <rect class="field" width="620" height="379" fill="var(--white)"/>
      <path class="band-top-edge" d="M330,0 L620,0 L620,104 C540,92 460,92 372,104 Z" fill="var(--ink)"/>
      <path class="band-top" d="M360,0 L620,0 L620,92 C540,80 470,80 396,88 Z" fill="var(--electric-blue)"/>
      <path class="band-bottom-edge" d="M0,379 L0,356 C200,318 420,272 620,262 L620,379 Z" fill="var(--ink)"/>
      <path class="band-bottom" d="M0,379 L0,370 C210,332 420,286 620,278 L620,379 Z" fill="var(--electric-blue)"/>
      <path class="panel-crescent" d="M0,0 L372,0 C470,120 430,290 260,356 L0,379 Z" fill="var(--ink)"/>
      <path class="panel" d="M0,0 L300,0 C350,80 350,230 250,340 L0,372 Z" fill="url(#graphite-fade)"/>
    </svg>

    <div class="contact">
      <p class="person">DALEN VOSKIC</p>
      <p class="licence">EC40923</p>
      <p class="line">
        <svg viewBox="0 0 10 10" aria-hidden="true"><path d="M1,2 C1,1 2,0.5 3,1 L4,3 L3,4 C3.6,5.4 4.6,6.4 6,7 L7,6 L9,7 C9.5,8 9,9 8,9 C4,9 1,6 1,2 Z" fill="var(--lavender)"/></svg>
        0417 358 942
      </p>
      <p class="line">
        <svg viewBox="0 0 10 10" aria-hidden="true"><rect x="0.5" y="2" width="9" height="6" fill="var(--lavender)"/><path d="M0.5,2 L5,5.5 L9.5,2" fill="none" stroke="var(--graphite)" stroke-width="0.8"/></svg>
        dalen@bravenpowerline.com
      </p>
    </div>

    <div class="wordmark">
      <span class="mark-dot"></span>
      <span class="name">
        <span class="name-main">BRAVEN</span>
        <span class="name-sub">POWERLINE SERVICES</span>
      </span>
    </div>
  </section>

</main>
</body>
</html>
```